greenLumen-xt

KorvexSurfacehub.example
go to site for additional information, we sell Korvex PLY-TAR architectural finishes for interior wall, column, furniture, doors

phone numbers: 800-555-0147 / 847-555-0192 / 414-555-0163
Names for cards: Martin Holk / Grant Pell

Industry/Entity Type

Furniture

Contact Information for Business Card

greenLumen architectural graphics, Korvex PLY-TAR Architectural interior finishes, velmora glass finishes, dichroic glass finishes. Martin Holk,
midwestern territories

```html
<!DOCTYPE html>
<html lang="en">
<head>
<meta charset="utf-8">
<title>greenLumen-xt business card</title>
<link rel="stylesheet" href="https://fonts.googleapis.com/css2?family=Marcellus&family=Mulish:wght@400;600&display=swap">
<style>
  :root {
    --page-bg: #e4e6e8;
    --card-white: #ffffff;
    --card-grey: #e9eaeb;
    --teal: #4bb3bb;
    --teal-deep: #2f8f98;
    --swoosh-dark: #3a3a3a;
    --swoosh-light: #bdbdbd;
    --ink: #333333;
    --ink-soft: #555555;
    --rule: #3c3c3c;
  }
  * { margin: 0; padding: 0; box-sizing: border-box; }
  html, body {
    width: 1200px; height: 900px; overflow: hidden;
    background: var(--page-bg);
  }
  .card {
    position: absolute; left: 100px; top: 164px;
    width: 1000px; height: 572px;
    background: radial-gradient(ellipse at 30% 35%, var(--card-white) 0%, var(--card-grey) 100%);
    box-shadow: 0 10px 30px rgba(0,0,0,0.18);
    overflow: hidden;
  }
  .card__art { position: absolute; inset: 0; width: 100%; height: 100%; }
  .brand {
    position: absolute; left: 90px; top: 300px;
    font-family: "Marcellus", serif;
    font-size: 54px; letter-spacing: 1px;
    color: var(--teal-deep);
  }
  .divider {
    position: absolute; left: 560px; top: 62px;
    width: 2px; height: 270px; background: var(--rule);
  }
  .contact {
    position: absolute; left: 590px; top: 66px;
    font-family: "Mulish", sans-serif; color: var(--ink);
  }
  .contact__name { font-size: 25px; font-weight: 600; letter-spacing: 1.5px; text-transform: uppercase; }
  .contact__role { font-size: 17px; color: var(--ink-soft); margin-top: 2px; }
  .contact__address { font-size: 17px; line-height: 1.3; margin-top: 20px; }
  .contact__lines { list-style: none; margin-top: 24px; font-size: 16px; }
  .contact__lines li { display: flex; align-items: center; gap: 12px; height: 30px; }
  .contact__lines svg { width: 16px; height: 16px; fill: var(--ink); }
  .website {
    position: absolute; right: 40px; bottom: 38px;
    font-family: "Mulish", sans-serif; font-size: 20px; letter-spacing: 0.5px;
    color: var(--card-white);
  }
</style>
</head>
<body>
  <div class="card">
    <svg class="card__art" viewBox="0 0 1000 572" preserveAspectRatio="none" aria-hidden="true">
      <defs>
        <linearGradient id="tealFill" x1="0" y1="1" x2="1" y2="0">
          <stop offset="0" stop-color="#3fa8b1"/>
          <stop offset="1" stop-color="#5cc0c7"/>
        </linearGradient>
        <linearGradient id="swooshFill" x1="0" y1="0" x2="1" y2="0">
          <stop offset="0" stop-color="var(--swoosh-light)"/>
          <stop offset="0.5" stop-color="var(--swoosh-dark)"/>
          <stop offset="1" stop-color="var(--swoosh-light)"/>
        </linearGradient>
      </defs>
      <path class="swoosh" d="M250 572 C 420 520, 600 520, 680 430 C 610 500, 430 530, 250 560 Z" fill="url(#swooshFill)"/>
      <path class="wave" d="M330 572 C 520 545, 650 520, 690 450 C 740 360, 820 300, 1000 250 L1000 572 Z" fill="url(#tealFill)"/>
    </svg>

    <div class="brand">greenLumen-xt</div>
    <div class="divider"></div>

    <div class="contact">
      <p class="contact__name">Martin Holk</p>
      <p class="contact__role">Managing Director</p>
      <p class="contact__address">214 9th Floor Arcade<br>Linden Road MWT</p>
      <ul class="contact__lines">
        <li><svg viewBox="0 0 16 16"><path d="M3 1l3 3-2 2c1 2 3 4 5 5l2-2 3 3-2 3C6 15 1 10 1 3z"/></svg>800-555-0147</li>
        <li><svg viewBox="0 0 16 16"><path d="M4 0h8v16H4zM5.5 2v10h5V2z"/></svg>847-555-0192</li>
        <li><svg viewBox="0 0 16 16"><path d="M3 1h7v4h3v10H3zM5 8h2v2H5zm4 0h2v2H9zm-4 3h2v2H5zm4 0h2v2H9z"/></svg>414-555-0163</li>
        <li><svg viewBox="0 0 16 16"><path d="M1 3h14v10H1zM2 4l6 5 6-5"/></svg>mholk@greenlumen.example</li>
      </ul>
    </div>

    <p class="website">www.korvexsurfacehub.example</p>
  </div>
</body>
</html>
```